Personal training and nutrition business needs business card design

We need a business card that outlays our services and invites potential customers to join our team and take the first step to a healthier and more enjoyable life. We cater for any level of fitness and specialize in weight loss and conditioning, strength training, muscle gain and strength endurance. Whether you are just starting off or need some help getting to the next level of your journey we are here to get the job done.
We specialize in one on one or one on two personal training sessions and each program will be custom made to suit individual fitness goals of our clients

```html
<!DOCTYPE html>
<html lang="en">
<head>
<meta charset="utf-8">
<title>Stride &amp; Current – Business Card</title>
<link rel="stylesheet" href="https://fonts.googleapis.com/css2?family=Oswald:wght@400;500;700&display=swap">
<style>
  :root {
    --backdrop: #2b2b2d;
    --card-dark: #050505;
    --card-light: #ffffff;
    --ink: #111111;
    --purple: #8b4fb8;
    --purple-deep: #6a3fa8;
    --purple-pink: #b55fc0;
    --tint-light: #efe7f5;
    --tint-dark: #111013;
    --white: #ffffff;
  }
  * { box-sizing: border-box; margin: 0; padding: 0; }
  html, body { width: 1200px; height: 900px; overflow: hidden; }
  body {
    background: var(--backdrop);
    font-family: "Oswald", sans-serif;
    position: relative;
  }
  .card {
    position: absolute;
    width: 630px;
    height: 360px;
    border-radius: 26px;
    overflow: hidden;
  }
  .card--front { left: 90px; top: 60px; background: var(--card-dark); }
  .card--back { left: 480px; top: 480px; background: var(--card-light); }

  .decor-block { position: absolute; border-radius: 40px; }
  .card--front .decor-block { left: -60px; top: 150px; width: 360px; height: 260px; background: var(--tint-dark); }
  .card--back .decor-block { right: -40px; top: 40px; width: 300px; height: 340px; background: var(--tint-light); }

  .brand {
    position: absolute;
    display: flex;
    flex-direction: column;
    align-items: flex-start;
  }
  .brand__mark {
    width: 46px; height: 46px; border-radius: 10px;
    margin-bottom: 12px;
    background: linear-gradient(135deg, var(--purple-deep), var(--purple-pink));
  }
  .brand__name {
    font-weight: 700;
    font-size: 40px;
    line-height: 1;
    text-transform: uppercase;
    letter-spacing: 1px;
  }
  .brand__tagline {
    margin-top: 10px;
    font-weight: 500;
    font-size: 11px;
    letter-spacing: 1.5px;
    color: var(--purple);
    text-transform: uppercase;
    white-space: nowrap;
  }
  .card--front .brand { left: 50%; top: 50%; transform: translate(-50%, -50%); }
  .card--front .brand__name { color: var(--white); }
  .card--back .brand { left: 40px; top: 92px; }
  .card--back .brand__name { color: var(--ink); }
  .card--back .brand__tagline { font-size: 10px; letter-spacing: 1px; }

  .divider {
    position: absolute;
    left: 320px; top: 60px;
    width: 2px; height: 240px;
    background: var(--purple);
  }
  .contact {
    position: absolute;
    left: 345px; top: 58px;
    color: var(--ink);
  }
  .contact__name { font-weight: 700; font-size: 26px; line-height: 1.1; text-transform: uppercase; }
  .contact__title { font-weight: 500; font-size: 16px; color: var(--purple); text-transform: uppercase; letter-spacing: .5px; margin-bottom: 12px; }
  .contact__address { font-size: 15px; line-height: 1.45; margin-bottom: 12px; }
  .contact__list { list-style: none; }
  .contact__item { display: flex; align-items: center; gap: 10px; font-size: 15px; margin-bottom: 8px; }
  .contact__icon {
    width: 20px; height: 20px; border-radius: 5px;
    background: var(--purple);
    display: flex; align-items: center; justify-content: center;
  }
  .contact__icon svg { width: 12px; height: 12px; }
</style>
</head>
<body>

<section class="card card--front" aria-label="Card front">
  <div class="decor-block"></div>
  <div class="brand">
    <span class="brand__mark"></span>
    <span class="brand__name">Stride &amp;<br>Current</span>
    <span class="brand__tagline">Personal Training. Nutrition. Motivation</span>
  </div>
</section>

<section class="card card--back" aria-label="Card back">
  <div class="decor-block"></div>
  <div class="brand">
    <span class="brand__mark"></span>
    <span class="brand__name">Stride &amp;<br>Current</span>
    <span class="brand__tagline">Personal Training. Nutrition. Motivation</span>
  </div>

  <div class="divider"></div>

  <div class="contact">
    <p class="contact__name">Daniel Reyes</p>
    <p class="contact__title">Managing Director</p>
    <p class="contact__address">418 Alder Lane<br>Suite 12, Millbrook<br>OR 97555</p>
    <ul class="contact__list">
      <li class="contact__item">
        <span class="contact__icon"><svg viewBox="0 0 24 24" fill="none" stroke="#fff" stroke-width="2.4" stroke-linecap="round" stroke-linejoin="round"><path d="M5 3h4l2 5-3 2a12 12 0 0 0 6 6l2-3 5 2v4a2 2 0 0 1-2 2A18 18 0 0 1 3 5a2 2 0 0 1 2-2z"/></svg></span>
        555-014-2290
      </li>
      <li class="contact__item">
        <span class="contact__icon"><svg viewBox="0 0 24 24" fill="none" stroke="#fff" stroke-width="2.4" stroke-linejoin="round"><rect x="2" y="5" width="20" height="14" rx="2"/><path d="M2 6l10 7 10-7"/></svg></span>
        dan@stridecurrent.com
      </li>
      <li class="contact__item">
        <span class="contact__icon"><svg viewBox="0 0 24 24" fill="none" stroke="#fff" stroke-width="2.2"><circle cx="12" cy="12" r="10"/><path d="M2 12h20M12 2c3 3 3 17 0 20M12 2c-3 3-3 17 0 20"/></svg></span>
        www.stridecurrent.com
      </li>
    </ul>
  </div>
</section>

</body>
</html>
```